Layout für Werbefahnen gesucht
Zielgruppe
Unsere Frühstückpension befindet sich in Jois am Neusiedlersee mit direktem Rebenhangblick. Wir haben auch ein Weingut was unsere Gäste sehr schätzen.
Unsere Zielgruppe sind Urlaubsgäste mit höheren Ansprüchen sowie Weinbegeistere , Naturliebhaber, Radfahrer und Seeliebhaber (Neusiedlersee) unser Haus wurde mit sehr hochwertigen Materialien ausgestattet.
Aufgabenstellung
3 STK Werbefahnen ( Fahnenmast stehen schon siehe Beilage Bild) Maße: Format 1000x4000 mm
Unser Logo sollte auf den Fahnen vorhanden sein, man soll erkennen - dass man hier Urlaub verbringen kann und Wein verkosten (genießen) oder auch kaufen kann.
Gerne mit netten kurzen Sprüchen oder Wortspielen (Urlaub mit Rebenhangblick oder so?.
Naturverbunden mit liebe zum Wein, die Farben sollten unserem Logo angepasst werden eher naturverbunden braun oder grün, 1 Fahne sollte nur für den Wein gestaltet werden und die anderen beiden für unser Gästehaus.

```html
<!DOCTYPE html>
<html lang="de">
<head>
<meta charset="utf-8">
<title>Werbefahnen – Gut Rebenhang</title>
<link href="https://fonts.googleapis.com/css2?family=EB+Garamond:wght@400;500&family=Open+Sans:wght@400;700&display=swap" rel="stylesheet">
<style>
  :root{
    --canvas:#ffffff;
    --cream:#efece6;
    --tan:#d2b8a0;
    --light:#f2eee8;
    --brown:#6b2a14;
    --olive:#8b8a1c;
    --sky:#4aa8e0;
    --bottle:#2a1f1d;
  }
  html,body{margin:0;padding:0;overflow:hidden;}
  body{width:1116px;height:1200px;background:var(--canvas);position:relative;}
  .flag{position:absolute;top:40px;width:283px;height:1135px;background:var(--cream);overflow:hidden;}
  .flag--nature{left:74px;}
  .flag--wine{left:428px;}
  .flag--stay{left:782px;}
  .flag-shapes{position:absolute;left:0;top:0;}
  .brand{position:absolute;top:100px;left:0;width:283px;text-align:center;
    font-family:"EB Garamond",serif;font-weight:500;font-size:30px;letter-spacing:1px;color:var(--brown);}
  .script{position:absolute;left:30px;top:478px;font-family:"EB Garamond",serif;font-weight:400;
    font-size:70px;line-height:58px;color:var(--light);white-space:nowrap;}
  .flag--wine .script{left:34px;}
  .flag--stay .script{left:37px;}
  .verb{position:absolute;font-family:"Open Sans",sans-serif;font-weight:700;font-size:94px;
    line-height:94px;color:var(--light);letter-spacing:2px;margin:0;}
  .bottle{position:absolute;left:212px;top:620px;width:42px;height:155px;}
  .offer{position:absolute;left:0;top:955px;width:283px;text-align:center;font-family:"Open Sans",sans-serif;
    font-weight:400;font-size:27px;line-height:50px;letter-spacing:1.5px;}
  .flag--nature .offer{color:var(--olive);}
  .flag--wine .offer{color:var(--brown);}
  .flag--stay .offer{color:var(--sky);}
</style>
</head>
<body>

<section class="flag flag--nature">
  <svg class="flag-shapes" width="283" height="1135" viewBox="0 0 283 1135">
    <defs>
      <linearGradient id="fieldTone" x1="0" y1="0" x2="0" y2="1">
        <stop offset="0" stop-color="#8cc2e6"/><stop offset="0.55" stop-color="#cfe0ea"/>
        <stop offset="0.7" stop-color="#6b8a3a"/><stop offset="1" stop-color="#b7c24a"/>
      </linearGradient>
    </defs>
    <path role="img" aria-label="Foto: Felder und Hügel unter blauem Himmel" fill="url(#fieldTone)"
      d="M0 238 C25 260 55 270 90 255 C130 238 170 215 220 222 C250 226 270 232 283 236 L283 477 L0 477 Z"/>
    <path fill="var(--tan)" d="M0 477 L283 477 L283 908 C250 890 225 935 190 935 C140 935 110 880 60 883 C30 885 12 895 0 905 Z"/>
  </svg>
  <div class="brand">GUT REBENHANG</div>
  <div class="script">die<br>Natur</div>
  <p class="verb" style="left:92px;top:603px;">ER</p>
  <p class="verb" style="left:34px;top:686px;">LE</p>
  <p class="verb" style="left:60px;top:769px;">BEN</p>
  <div class="offer">RADFAHREN<br>WANDERN<br>SEE-AKTIVITÄTEN</div>
</section>

<section class="flag flag--wine">
  <svg class="flag-shapes" width="283" height="1135" viewBox="0 0 283 1135">
    <defs>
      <linearGradient id="vineTone" x1="0" y1="0" x2="0" y2="1">
        <stop offset="0" stop-color="#8cc2e6"/><stop offset="0.6" stop-color="#c9dbe3"/>
        <stop offset="0.72" stop-color="#557a45"/><stop offset="1" stop-color="#3f6a3a"/>
      </linearGradient>
    </defs>
    <path role="img" aria-label="Foto: Weingarten mit Blick auf den See" fill="url(#vineTone)"
      d="M0 238 C25 260 55 270 90 255 C130 238 170 215 220 222 C250 226 270 232 283 236 L283 477 L0 477 Z"/>
    <path fill="var(--tan)" d="M0 477 L283 477 L283 908 C250 890 225 935 190 935 C140 935 110 880 60 883 C30 885 12 895 0 905 Z"/>
  </svg>
  <div class="brand">GUT REBENHANG</div>
  <div class="script">mit den<br>Sinnen</div>
  <p class="verb" style="left:84px;top:603px;">GE</p>
  <p class="verb" style="left:32px;top:686px;">NIE</p>
  <p class="verb" style="left:60px;top:769px;">ßEN</p>
  <svg class="bottle" viewBox="0 0 42 155" role="img" aria-label="Foto: Weinflasche">
    <path fill="var(--bottle)" d="M15 0 H27 V40 C27 52 42 58 42 80 V150 Q42 155 37 155 H5 Q0 155 0 150 V80 C0 58 15 52 15 40 Z"/>
  </svg>
  <div class="offer">VERKOSTUNG<br>&amp;<br>VERKAUF</div>
</section>

<section class="flag flag--stay">
  <svg class="flag-shapes" width="283" height="1135" viewBox="0 0 283 1135">
    <defs>
      <linearGradient id="lakeTone" x1="0" y1="0" x2="0" y2="1">
        <stop offset="0" stop-color="#7fbbe6"/><stop offset="0.6" stop-color="#b9d8ec"/>
        <stop offset="0.68" stop-color="#3a6fa0"/><stop offset="1" stop-color="#1f3f66"/>
      </linearGradient>
    </defs>
    <path role="img" aria-label="Foto: Yachthafen am See mit Schilf" fill="url(#lakeTone)"
      d="M0 238 C25 260 55 270 90 255 C130 238 170 215 220 222 C250 226 270 232 283 236 L283 477 L0 477 Z"/>
    <path fill="var(--tan)" d="M0 477 L283 477 L283 908 C250 890 225 935 190 935 C140 935 110 880 60 883 C30 885 12 895 0 905 Z"/>
  </svg>
  <div class="brand">GUT REBENHANG</div>
  <div class="script">einfach<br>nur</div>
  <p class="verb" style="left:90px;top:603px;">ER</p>
  <p class="verb" style="left:36px;top:686px;">HO</p>
  <p class="verb" style="left:62px;top:769px;">LEN</p>
  <div class="offer">URLAUB<br>MIT<br>REBENHANGBLICK</div>
</section>

</body>
</html>
```